Corporate Identity Design Project

Marisol Tevendry Design is a small boutique event planning and floral design company, based in Northern Alberta. I require the creation of some corporate identity pieces. I want a minimalistic design.
Website www.marisoltevendry.com

Pieces should include
1. Business Card
Should include the company logo, name, email address, address, phone number. These will be professional printed.
These are three cards that I like:
http://cardlayoutgallerynook.com/wp-content/uploads/2010/02/Renata_Voskuilen_Roomworks_by_Pepperleaf_studio_Graphics.jpg
http://tidycardshowcase.com/wp-content/uploads/2011/06/Quietfold-Studio-Minimalist-Business-Cards_11.jpg
http://graphiclanternhub.com/wp-content/uploads/2012/03/16.minimalist-business-cards.jpg
I like letterpress, but I am open to other options.

2. Letterhead
will be professionally printed

3. Envelope

4. Fax Sheet
will be printed on home printer

5. Pocket Presentation
Like -http://fernwickgardenworks.com/img/design_step_proposal@2x.jpg

6. Invoice
Like - http://velmaquorlin.files.blogsite-example.com/2011/02/summit-strength-4-letterhead-combined.png?w=529

7. Proposal
Like something like this – this will not be printed, but rather emailed to clients
Like http://getfile7.brindlepost.com/getfile/files.brindlepost.com/tarnu-studio/qwRtZe8MmXp3LoKcV7B2nhdYJsaWeFUy6gT4rkPHvxiQbNcDzA9jsLE/Picture-52.png.scaled.500.jpg

8. Contract
Like http://www.brightkeelpromo.co.uk/images/tamsin-contract.jpg

9. Business Brochure – I have removed this piece from the project and will most likely post it as another project at a later date.

If you think that this is a project of interest to you, but feel that it is “too much” work for the price, please let me know how you would re-package it – I am open to suggestions.

Target Market(s)

Young women

Industry/Entity Type

Boutique

Requirements
Should not have
• I do not want it to look "frilly"

```html
<!DOCTYPE html>
<html lang="en">
<head>
<meta charset="utf-8">
<title>Marisol Tevendry Design — Pocket Presentation Folder</title>
<link rel="stylesheet" href="https://fonts.googleapis.com/css2?family=Josefin+Sans:wght@400&display=swap">
<style>
  :root {
    --backdrop: #e2e2e2;
    --mauve-light: #9a5f61;
    --mauve-dark: #7c4b4d;
    --folder-black: #121212;
    --folder-black-soft: #1c1c1c;
    --ink-light: #ffffff;
    --accent-rose: #c98a8c;
  }
  html, body {
    margin: 0;
    padding: 0;
    width: 1200px;
    height: 939px;
    overflow: hidden;
    background: var(--backdrop);
  }
  .canvas {
    position: relative;
    width: 1200px;
    height: 939px;
  }
  .folder {
    position: absolute;
    left: 280px;
    top: 185px;
    width: 640px;
    height: 570px;
    display: flex;
  }
  .folder__cover {
    width: 340px;
    height: 570px;
    background: linear-gradient(90deg, var(--mauve-light), var(--mauve-dark));
  }
  .folder__back {
    position: relative;
    width: 300px;
    height: 570px;
  }
  .folder__back-shape {
    position: absolute;
    inset: 0;
    display: block;
  }
  .brand {
    position: absolute;
    left: 40px;
    top: 110px;
    display: flex;
    align-items: center;
    gap: 12px;
  }
  .brand__dot {
    width: 26px;
    height: 26px;
    border-radius: 50%;
    background: var(--accent-rose);
    flex: none;
  }
  .brand__name {
    margin: 0;
    font-family: "Josefin Sans", sans-serif;
    font-weight: 400;
    font-size: 14px;
    line-height: 1.2;
    letter-spacing: 0.12em;
    text-transform: uppercase;
    color: var(--ink-light);
    width: 140px;
  }
</style>
</head>
<body>
  <main class="canvas">
    <section class="folder" aria-label="Pocket presentation folder, opened flat">
      <div class="folder__cover" aria-label="Folder front cover"></div>
      <div class="folder__back">
        <svg class="folder__back-shape" width="300" height="570" viewBox="0 0 300 570" aria-hidden="true">
          <defs>
            <linearGradient id="backFill" x1="0" y1="0" x2="1" y2="0">
              <stop offset="0" stop-color="#121212"/>
              <stop offset="1" stop-color="#1c1c1c"/>
            </linearGradient>
          </defs>
          <path d="M0 0 H300 V45 C300 140, 285 185, 258 255 C232 320, 222 370, 222 420 V570 H0 Z" fill="url(#backFill)"/>
        </svg>
        <div class="brand">
          <span class="brand__dot"></span>
          <p class="brand__name">Marisol Tevendry Design</p>
        </div>
      </div>
    </section>
  </main>
</body>
</html>
```